Website to showcase Pram Dash Days that will be held in Woodland Trustees areas in the UK

Looking for a website, designed in WordPress, to provide information on family orientated running events that I'm organising in the UK (I've registered the website address pramdashdays.co.uk). Refer to the Project Brief document however as a summary:
These events are unique, as they are for people running with a child in a buggy (or in a wheelchair) and will be on carefully designed, traffic-free courses in Woodland Trustees areas. The events, by using a specialist timing system, will allow runners to start within a two hour window therefore removing the anxiety / rush to get to the start line for the mass start. All events will be centred around a family day with face painting, adventure playgrounds, café and ample parking. Current thinking is a home page that will contain links to four separate pages, information about me and a blog from my Chatterbox and Chirpline feeds, one page for two running events being held at Fern Cottage, Marlow Wood (www.woodlandtrustees.example/ferncottage) in October and December and another page for an event at Edith Vane Wood (www.woodlandtrustees.example/edithvane) in November. The third page will be information on the different running buggies available and how people can come and view them at each event and try them out on the course and if they like it they can purchase that buggy for a 10% discount of the RRP. They will need to email me to reserve a buggy for use at the event. The forth page will be information on myself ('About Me' and the details from my other website can be used at this stage). There will be a link from each event page to allow people to enter that particular race online from an external website (links to follow). My current website is an online shop selling running buggies (www.pramdash.co.uk).

I'm also looking for the website to be published (access to cPanel will be given to allow this).

Attached is my current logo (this will be replaced by a new one currently being designed but is nearly identical) so will be replaced before the website goes live. Also attached are a couple of photos to give an idea on running with a buggy and the different types of areas being used. One of the pictures is the lineup of running buggies so could be used on the third page as it was taken at one of the event forests. Also attached are two logos for the Woodland Trustees that should be on the home page.

Alongside the website I'm also looking for two flyers to be designed to showcase each running event (to be used on Social Media and public locations such as cafes, nurseries, running clubs, gyms). One flyer for Fern Cottage Marlow Wood event on the 1st October 2017 and the second flyer for the Edith Vane Wood event on the 5th November 2017. Both these flyers will be a separate project and therefore attract additional payment for each. Will look to offer this work to the winning designer.

Target Market(s)

Families

Industry/Entity Type

Events

Number of Pages Required

5+ page

Font styles to use
Sans Serif

Colors

Designer to choose colors to be used in the design.

Requirements
Must have
• Clear and precise information that each Pram Dash event is family orientated, on an off-road course that has been carefully planned to be used by a buggy. Different page to highlight the event (i've taken a video of each course so people can see what the terrain is like), course map, course distance, hill profile, timings for the day, travel directions, course dates in 2017 and 2018.
• I'm also looking for the website to be published (access to cPanel will be given to allow this).
• Countdown timer to the next event.
Nice to have
• Map of the UK with the locations highlighted (with a link to the event page). More locations to follow during the rest of 2017.
Should not have
• A lot of writing in small font

```html
<!DOCTYPE html>
<html lang="en">
<head>
<meta charset="utf-8">
<title>Pram Dash Days</title>
<link rel="stylesheet" href="https://fonts.googleapis.com/css2?family=Open+Sans:ital,wght@0,400;0,600;0,700;1,400&display=swap">
<style>
:root{
  --orange:#f07d1c;
  --ink:#333333;
  --muted:#777777;
  --line:#e2e2e2;
  --panel-bg:#ececec;
  --footer:#0e0e0e;
  --white:#ffffff;
  --green:#7bb23a;
  --blue:#3b5a99;
  --font:"Open Sans",Arial,sans-serif;
}
*{box-sizing:border-box;margin:0;padding:0}
html,body{width:1200px;height:3584px;overflow:hidden}
body{font-family:var(--font);color:var(--ink);background:var(--white);position:relative}
.abs{position:absolute}
a{color:inherit;text-decoration:none}

/* header */
.site-header{left:0;top:0;width:1200px;height:112px;background:var(--white)}
.brand{left:40px;top:36px;display:flex;align-items:center;gap:12px}
.brand-name{font-size:26px;font-weight:600;color:var(--ink)}
.main-nav{right:40px;top:44px;display:flex;gap:30px;font-size:15px;font-weight:600;color:var(--ink)}
.main-nav .current{color:var(--orange);border-bottom:2px solid var(--orange);padding-bottom:6px}

/* hero */
.hero{left:0;top:112px;width:1200px;height:650px;background:linear-gradient(180deg,#6f8a5a 0%,#8fa477 40%,#5d6b4a 75%,#4a5039 100%)}
.hero-title{left:0;top:330px;width:1200px;text-align:center;color:var(--white);font-size:56px;font-weight:700;letter-spacing:2px;text-shadow:0 2px 6px rgba(0,0,0,.4)}
.hero-sub{left:0;top:412px;width:1200px;text-align:center;color:var(--white);font-size:28px;text-shadow:0 2px 6px rgba(0,0,0,.4)}
.hero-wave{left:0;top:640px;width:1200px;height:130px}

/* welcome */
.section-title{width:1200px;left:0;text-align:center;font-size:36px;font-weight:400;color:var(--ink)}
.welcome-text{left:300px;top:840px;width:600px;text-align:center;font-size:13px;line-height:20px;color:var(--muted)}
.feature{width:300px;display:flex;gap:12px}
.feature svg{flex:none}
.feature h3{font-size:18px;font-weight:600;color:var(--ink);margin-bottom:6px}
.feature p{font-size:12px;line-height:18px;color:var(--muted);margin-bottom:6px}
.read-more{font-size:12px;font-weight:600;color:var(--ink)}

/* about */
.about-band{left:0;top:1130px;width:1200px;height:345px;background:linear-gradient(90deg,#8a7c6a 0%,#6f665a 40%,#2a2a2a 58%,#1a1a1a 100%)}
.about-title{left:730px;top:1170px;font-size:40px;font-weight:400;color:var(--white)}
.about-text{left:730px;top:1240px;width:420px;font-size:13px;line-height:20px;color:#dddddd}
.btn-outline{left:730px;top:1370px;padding:8px 20px;border:1px solid var(--white);border-radius:20px;font-size:12px;color:var(--white)}

/* events */
.event-card{width:290px;top:1700px;background:var(--white);text-align:center}
.event-photo{height:170px;position:relative}
.event-date{position:absolute;left:0;bottom:0;background:var(--orange);color:var(--white);font-size:11px;font-weight:600;padding:4px 10px}
.event-card h3{font-size:17px;font-weight:600;margin:14px 0 6px}
.event-card p{font-size:12px;line-height:18px;color:var(--muted);padding:0 20px}
.event-card .read-more{display:block;margin-top:4px;color:var(--orange);font-weight:400}
.arrow{width:36px;height:36px;border-radius:50%;background:#f2f2f2;display:flex;align-items:center;justify-content:center}

/* reviews */
.reviews-band{left:0;top:2040px;width:1200px;height:395px;background:linear-gradient(135deg,#e47a14 0%,#f39b2f 45%,#d8690d 100%)}
.reviews-title{left:0;top:2080px;width:1200px;text-align:center;font-size:36px;font-weight:400;color:var(--white)}
.quote{left:300px;top:2160px;width:600px;text-align:center;font-size:13px;line-height:20px;font-style:italic;color:var(--white)}
.avatar{left:560px;top:2295px;width:80px;height:80px;border-radius:50%;border:3px solid var(--white);background:linear-gradient(160deg,#c9a98a,#8b6a52)}
.reviewer{left:0;top:2385px;width:1200px;text-align:center;font-size:12px;color:var(--white)}

/* social panels */
.panels{left:0;top:2510px;width:1200px;height:460px;background:var(--panel-bg)}
.panel{top:2580px;height:340px;background:var(--white);box-shadow:0 1px 4px rgba(0,0,0,.15)}
.panel-head{height:40px;display:flex;align-items:center;padding:0 14px;font-size:15px;font-weight:600;color:var(--white)}
.map-area{height:300px;background:linear-gradient(180deg,#dcdcd6,#cfcfc8);position:relative}
.feed-row{display:flex;gap:10px;padding:10px 14px;border-bottom:1px solid var(--line)}
.feed-thumb{width:40px;height:40px;flex:none;background:linear-gradient(135deg,#9db07e,#61704e)}
.feed-row p{font-size:11px;line-height:15px;color:var(--muted)}
.feed-row b{color:var(--blue);font-weight:600}

/* partners */
.partner-a{left:190px;top:3000px;width:200px;height:100px;background:var(--green);transform:rotate(-3deg)}
.partner-b{left:570px;top:3010px;width:440px;height:80px;background:var(--green);transform:rotate(-3deg)}
.partner-b::after{content:"";position:absolute;right:0;top:0;width:210px;height:80px;background:var(--orange)}

/* footer */
.site-footer{left:0;top:3150px;width:1200px;height:434px;background:var(--footer)}
.footer-brand{left:0;top:3215px;width:1200px;text-align:center;font-size:26px;font-weight:600;color:var(--white)}
.social{left:0;top:3320px;width:1200px;display:flex;justify-content:center;gap:18px}
.social span{width:38px;height:38px;border-radius:50%;background:#3a3a3a}
.social span:first-child{background:var(--orange)}
.footer-rule{left:0;top:3420px;width:1200px;height:1px;background:#2c2c2c}
.copyright{left:0;top:3450px;width:1200px;text-align:center;font-size:12px;color:#999999}
</style>
</head>
<body>

<header class="site-header abs">
  <div class="brand abs"><span class="brand-name">Pram Dash Days</span></div>
  <nav class="main-nav abs">
    <a class="current">Home</a><a>About us</a><a>Fern Cottage running event</a><a>Edith Vane running event</a><a>Our information</a>
  </nav>
</header>

<section class="hero abs" role="img" aria-label="Photo of a child in a running buggy on a forest lawn"></section>
<h1 class="hero-title abs">PRAM DASH DAYS</h1>
<p class="hero-sub abs">Neque porro quisquam dolorem</p>
<svg class="hero-wave abs" viewBox="0 0 1200 130" preserveAspectRatio="none">
  <path d="M0 40 Q600 140 1200 20 L1200 130 L0 130 Z" fill="#ffffff"/>
  <path d="M0 40 Q600 140 1200 20" fill="none" stroke="#f07d1c" stroke-width="6"/>
</svg>

<h2 class="section-title abs" style="top:780px">Welcome to Pram Dash Days</h2>
<p class="welcome-text abs">It is a long established fact that a reader will be distracted by the readable content of a page when looking at its layout. The point of using sample text is that it has a more-or-less normal distribution of letters, as opposed to using content here, making it look like readable English for every visitor.</p>

<div class="feature abs" style="left:130px;top:960px">
  <svg width="26" height="26" viewBox="0 0 24 24"><path d="M12 2a7 7 0 0 0-7 7c0 5 7 13 7 13s7-8 7-13a7 7 0 0 0-7-7zm0 9.5A2.5 2.5 0 1 1 12 6.5a2.5 2.5 0 0 1 0 5z" fill="#f07d1c"/></svg>
  <div><h3>Fern Cottage running event</h3><p>Lorem ipsum has been the industry's standard dummy text ever since.</p><a class="read-more">Read More ›</a></div>
</div>
<div class="feature abs" style="left:470px;top:960px">
  <svg width="26" height="26" viewBox="0 0 24 24"><rect x="3" y="5" width="18" height="16" rx="2" fill="none" stroke="#f07d1c" stroke-width="2"/><path d="M3 10h18M8 3v4M16 3v4" stroke="#f07d1c" stroke-width="2"/></svg>
  <div><h3>Edith Vane running event</h3><p>Lorem ipsum has been the industry's standard dummy text ever since.</p><a class="read-more">Read More ›</a></div>
</div>
<div class="feature abs" style="left:800px;top:960px">
  <svg width="26" height="26" viewBox="0 0 24 24"><rect x="2" y="4" width="20" height="13" rx="1" fill="none" stroke="#f07d1c" stroke-width="2"/><path d="M8 21h8M12 17v4" stroke="#f07d1c" stroke-width="2"/></svg>
  <div><h3>Our information</h3><p>Lorem ipsum has been the industry's standard dummy text ever since.</p><a class="read-more">Read More ›</a></div>
</div>

<section class="about-band abs" role="img" aria-label="Photo of a line of running buggies on a grass field in front of a lodge"></section>
<h2 class="about-title abs">About us</h2>
<p class="about-text abs">It was popularised in the 1960s with the release of sheets containing sample passages, and more recently with desktop publishing software including versions of sample text. It has survived not only five centuries but also the leap into electronic typesetting, remaining essentially unchanged for all readers.</p>
<a class="btn-outline abs">Read More ›</a>

<h2 class="section-title abs" style="top:1590px">Upcoming Events</h2>
<div class="arrow abs" style="left:40px;top:1830px"><svg width="12" height="12" viewBox="0 0 12 12"><path d="M8 1L3 6l5 5" fill="none" stroke="#777" stroke-width="2"/></svg></div>
<div class="arrow abs" style="left:1124px;top:1830px"><svg width="12" height="12" viewBox="0 0 12 12"><path d="M4 1l5 5-5 5" fill="none" stroke="#777" stroke-width="2"/></svg></div>

<article class="event-card abs" style="left:150px">
  <div class="event-photo" role="img" aria-label="Photo of runners pushing buggies on a forest track" style="background:linear-gradient(160deg,#8fae6a,#4f6b3a)"><span class="event-date">Oct 2017</span></div>
  <h3>Porro quisquam</h3>
  <p>It has survived not only five centuries, but also the leap into electronic typesetting.</p>
  <a class="read-more">Read more</a>
</article>
<article class="event-card abs" style="left:455px">
  <div class="event-photo" role="img" aria-label="Photo of a family group at a running event" style="background:linear-gradient(160deg,#c98a52,#6b4a36)"><span class="event-date">Nov 2017</span></div>
  <h3>Dolorem ipsum</h3>
  <p>It has survived not only five centuries, but also the leap into electronic typesetting.</p>
  <a class="read-more">Read more</a>
</article>
<article class="event-card abs" style="left:760px">
  <div class="event-photo" role="img" aria-label="Photo of a buggy runner on an open grass course" style="background:linear-gradient(160deg,#a6c27a,#5f7d40)"><span class="event-date">Dec 2017</span></div>
  <h3>Neque porro</h3>
  <p>It has survived not only five centuries, but also the leap into electronic typesetting.</p>
  <a class="read-more">Read more</a>
</article>

<section class="reviews-band abs" role="img" aria-label="Orange textured background"></section>
<h2 class="reviews-title abs">Customers Reviews</h2>
<p class="quote abs">“It is a long established fact that a reader will be distracted by the readable content of a page when looking at its layout. The point of using sample text is that it has a more-or-less normal distribution of letters, as opposed to using content here, content here, making it look like readable English.”</p>
<svg class="abs" style="left:525px;top:2325px" width="14" height="20" viewBox="0 0 14 20"><path d="M11 2L3 10l8 8" fill="none" stroke="#fff" stroke-width="2"/></svg>
<div class="avatar abs" role="img" aria-label="Reviewer portrait"></div>
<svg class="abs" style="left:661px;top:2325px" width="14" height="20" viewBox="0 0 14 20"><path d="M3 2l8 8-8 8" fill="none" stroke="#fff" stroke-width="2"/></svg>
<p class="reviewer abs">Jane Morrow, Runner</p>

<section class="panels abs"></section>

<div class="panel abs" style="left:100px;width:320px">
  <div class="panel-head" style="background:#4a4a4a">Location for running events</div>
  <div class="map-area" role="img" aria-label="Street map showing event locations">
    <svg class="abs" style="left:80px;top:110px" width="28" height="36" viewBox="0 0 24 32"><path d="M12 0a11 11 0 0 0-11 11c0 8 11 21 11 21s11-13 11-21A11 11 0 0 0 12 0z" fill="#e0504a"/><circle cx="12" cy="11" r="4" fill="#fff"/></svg>
    <svg class="abs" style="left:200px;top:210px" width="28" height="36" viewBox="0 0 24 32"><path d="M12 0a11 11 0 0 0-11 11c0 8 11 21 11 21s11-13 11-21A11 11 0 0 0 12 0z" fill="#e0504a"/><circle cx="12" cy="11" r="4" fill="#fff"/></svg>
  </div>
</div>

<div class="panel abs" style="left:450px;width:300px">
  <div class="panel-head" style="background:#3b5a99">Chatterbox Activity</div>
  <div class="feed-row"><p><b>Log in</b> to see what your friends are sharing on this site.</p></div>
  <div class="feed-row"><span class="feed-thumb"></span><p><b>Anna Reed</b> posted an update on the upcoming event.</p></div>
  <div class="feed-row"><span class="feed-thumb"></span><p><b>Tom Hale</b> shared a photo from the course walk.</p></div>
  <div class="feed-row"><span class="feed-thumb"></span><p><b>Lucy Park</b> liked the new buggy trial day.</p></div>
  <div class="feed-row"><span class="feed-thumb"></span><p><b>Sam Ford</b> commented on the race timings.</p></div>
</div>

<div class="panel abs" style="left:790px;width:310px">
  <div class="panel-head" style="background:#f7f7f7;color:#333;justify-content:space-between">Chirpline Updates<span style="font-size:11px;background:#dfe8f0;color:#333;padding:3px 8px;border-radius:3px">Follow</span></div>
  <div class="feed-row"><span class="feed-thumb"></span><p><b>pramdashdays</b> Entries now open for the autumn run.</p></div>
  <div class="feed-row"><span class="feed-thumb"></span><p><b>pramdashdays</b> New course map added to the site.</p></div>
  <div class="feed-row"><span class="feed-thumb"></span><p><b>pramdashdays</b> Try a running buggy at our next event.</p></div>
</div>

<div class="partner-a abs" role="img" aria-label="Woodland Trustees partner badge"></div>
<div class="partner-b abs" role="img" aria-label="Woodland Trustees outdoor activity badge"></div>

<footer class="site-footer abs"></footer>
<p class="footer-brand abs">Pram Dash Days</p>
<div class="social abs"><span></span><span></span><span></span><span></span><span></span><span></span></div>
<div class="footer-rule abs"></div>
<p class="copyright abs">Copyright © 2017 All Rights Reserved</p>

</body>
</html>
```